Brova Equipment Sales & Rentals

We are an independent equipment dealership located in the upstate of South Carolina. Our services include Equipment Sales, Equipment Rentals, Metal Sales, and Industrial Supplies.

I have attached our logos and a few billboards that we like as examples for inspiration. Thank you!

Phone Number 864-555-0172

Website link if you want to check out our page.
https://www.brovaequip.example

```html
<!DOCTYPE html>
<html lang="en">
<head>
<meta charset="utf-8">
<title>Brova Equipment Sales &amp; Rentals – Billboard</title>
<link href="https://fonts.googleapis.com/css2?family=Montserrat:wght@500;600;700;800;900&display=swap" rel="stylesheet">
<style>
  :root {
    --page-bg: #eef0f3;
    --board-top: #ffffff;
    --board-bottom: #dcdcdc;
    --brand-red: #e31b23;
    --ink: #1a1a1a;
    --white: #ffffff;
    --machine-yellow: #e0c23a;
    --machine-orange: #f06a1c;
    --machine-earth: #5a4a36;
  }
  * { box-sizing: border-box; margin: 0; padding: 0; }
  html, body {
    width: 1200px; height: 1200px; overflow: hidden;
    background: var(--page-bg);
    font-family: "Montserrat", Arial, sans-serif;
  }
  .billboard {
    position: absolute; left: 40px; top: 430px;
    width: 1120px; height: 340px;
    background: linear-gradient(180deg, var(--board-top) 0%, var(--board-bottom) 100%);
    overflow: hidden;
    box-shadow: 0 6px 20px rgba(0,0,0,.18);
  }
  .brand {
    position: absolute; left: 30px; top: 36px;
    display: flex; align-items: center; gap: 18px;
  }
  .brand-mark {
    width: 70px; height: 70px; background: var(--brand-red);
  }
  .brand-name {
    font-size: 112px; font-weight: 900; line-height: 1;
    color: var(--ink); letter-spacing: -1px;
  }
  .services {
    position: absolute; top: 186px;
    border-left: 2px solid var(--brand-red);
    padding-left: 8px;
    font-size: 21px; font-weight: 500; line-height: 1.15;
    color: var(--ink); text-transform: uppercase;
  }
  .services.col-equipment { left: 30px; }
  .services.col-supplies { left: 290px; }
  .services strong { color: var(--brand-red); font-weight: 700; }
  .red-band {
    position: absolute; left: 0; right: 0; top: 240px; height: 60px;
    background: var(--brand-red);
  }
  .phone {
    position: absolute; left: 28px; top: 236px;
    display: flex; align-items: center; gap: 10px;
    color: var(--white); font-size: 56px; font-weight: 800; line-height: 68px;
  }
  .phone svg { width: 34px; height: 34px; }
  .website {
    position: absolute; left: 70px; top: 302px;
    font-size: 28px; font-weight: 700; color: var(--ink);
  }
  .website .domain { color: var(--brand-red); }
  .equipment-photo {
    position: absolute; right: 0; top: 0;
    width: 540px; height: 310px;
    background: linear-gradient(100deg, var(--machine-yellow) 0%, var(--machine-earth) 35%, var(--machine-orange) 70%, var(--machine-earth) 100%);
  }
</style>
</head>
<body>
  <section class="billboard">
    <div class="brand">
      <span class="brand-mark"></span>
      <span class="brand-name">BROVA</span>
    </div>

    <p class="services col-equipment">Equipment <strong>Sales</strong><br>Equipment <strong>Rentals</strong></p>
    <p class="services col-supplies">Metal <strong>Sales</strong><br>Industrial <strong>Supplies.</strong></p>

    <div class="red-band"></div>
    <div class="phone">
      <svg viewBox="0 0 24 24" fill="none" stroke="#fff" stroke-width="2.2" stroke-linecap="round" stroke-linejoin="round" aria-hidden="true">
        <path d="M6 3h3l1.5 4-2 1.5a11 11 0 0 0 5 5l1.5-2 4 1.5v3a2 2 0 0 1-2 2A16 16 0 0 1 4 5a2 2 0 0 1 2-2z"/>
        <path d="M15 3a6 6 0 0 1 6 6M15 7a2 2 0 0 1 2 2"/>
      </svg>
      <span>864-555-0172</span>
    </div>
    <p class="website">www.<span class="domain">brovaequip</span>.example</p>

    <div class="equipment-photo" role="img" aria-label="Yellow and orange tracked excavators with buckets raised"></div>
  </section>
</body>
</html>
```